Billboard For Marcus Delvane

Need a Billboard 8ft. High x 16ft. Long. Ive attached a former billboard and looking for the same thing just updated with:
Wardens Guild Award Logo - 2020, 2022
Summit Lantern award Logo - 2022

Thanks.

```html
<!DOCTYPE html>
<html lang="en">
<head>
<meta charset="utf-8">
<title>Billboard – Marcus Delvane</title>
<link rel="stylesheet" href="https://fonts.googleapis.com/css2?family=Jost:ital,wght@0,300;0,400;0,600;0,700;0,800;1,700;1,800&family=Oswald:wght@300;400;600&display=swap">
<style>
  :root {
    --ink: #0b0b0b;
    --paper: #ffffff;
    --signal-red: #e3151f;
    --stage: #e8ecf1;
    --portrait-top: #7a6a60;
    --portrait-bottom: #3b55a6;
  }
  * { margin: 0; padding: 0; box-sizing: border-box; }
  html, body {
    width: 1200px;
    height: 800px;
    overflow: hidden;
    background: var(--stage);
  }
  .billboard {
    position: absolute;
    left: 40px;
    top: 120px;
    width: 1120px;
    height: 560px;
    display: block;
  }
  .billboard-face { fill: var(--paper); }
  .name-band { fill: var(--ink); }
  .tagline-band { fill: var(--signal-red); }

  .headline {
    font-family: "Jost", sans-serif;
    font-weight: 800;
    font-style: italic;
    font-size: 98px;
    fill: var(--ink);
  }
  .headline .call { fill: var(--signal-red); }

  .agent-name {
    font-family: "Jost", sans-serif;
    font-weight: 600;
    font-size: 98px;
    fill: var(--paper);
  }
  .agent-title {
    font-family: "Jost", sans-serif;
    font-weight: 600;
    font-size: 36px;
    fill: var(--signal-red);
  }
  .title-rule { stroke: var(--paper); stroke-width: 1.2; }
  .agent-phone {
    font-family: "Jost", sans-serif;
    font-weight: 600;
    font-size: 122px;
    fill: var(--paper);
  }
  .tagline {
    font-family: "Jost", sans-serif;
    font-weight: 700;
    font-size: 45px;
    fill: var(--paper);
  }
  .tagline .emphasis { font-style: italic; }

  .badge-ring { fill: none; stroke: var(--ink); stroke-width: 2; }
  .badge-core { fill: var(--ink); }
  .brokerage {
    font-family: "Jost", sans-serif;
    font-weight: 300;
    font-size: 18px;
    fill: var(--ink);
  }
  .award-name {
    font-family: "Oswald", sans-serif;
    font-weight: 400;
    font-size: 44px;
    fill: var(--ink);
  }
  .award-name.light { font-weight: 300; }
  .award-rule { stroke: var(--ink); stroke-width: 1.5; }
  .award-note {
    font-family: "Jost", sans-serif;
    font-weight: 400;
    font-size: 10px;
    fill: var(--ink);
  }
  .award-years {
    font-family: "Jost", sans-serif;
    font-weight: 700;
    font-size: 15px;
    fill: var(--ink);
  }
  .social-name {
    font-family: "Jost", sans-serif;
    font-weight: 600;
    font-size: 22px;
    fill: var(--signal-red);
  }
  .social-rule { stroke: var(--ink); stroke-width: 1.5; }
</style>
</head>
<body>
<svg class="billboard" viewBox="0 0 1371 685" xmlns="http://www.w3.org/2000/svg" aria-label="Billboard for Marcus Delvane, sales representative">
  <defs>
    <linearGradient id="portrait-tone" x1="0" y1="0" x2="0" y2="1">
      <stop offset="0" stop-color="var(--portrait-top)"/>
      <stop offset="0.5" stop-color="#b08a78"/>
      <stop offset="0.62" stop-color="var(--portrait-bottom)"/>
      <stop offset="1" stop-color="var(--portrait-bottom)"/>
    </linearGradient>
  </defs>

  <rect class="billboard-face" x="0" y="0" width="1371" height="685"/>

  <text class="headline" x="56" y="122" textLength="1267" lengthAdjust="spacingAndGlyphs">BUYING OR SELLING? <tspan class="call">CALL</tspan></text>

  <rect class="name-band" x="313" y="151" width="1058" height="321"/>
  <rect class="tagline-band" x="313" y="472" width="1058" height="67"/>

  <path class="agent-portrait" role="img" aria-label="Portrait photo of Marcus Delvane in a blue shirt and tie"
        fill="url(#portrait-tone)"
        d="M0 685 V505 Q0 470 60 450 L105 430 V195 Q105 130 230 130 Q358 130 358 195 V470 Q450 490 480 540 L530 685 Z"/>

  <text class="agent-name" x="853" y="262" text-anchor="middle" textLength="768" lengthAdjust="spacingAndGlyphs">MARCUS DELVANE</text>

  <line class="title-rule" x1="450" y1="300" x2="553" y2="300"/>
  <text class="agent-title" x="846" y="311" text-anchor="middle" textLength="558" lengthAdjust="spacing">SALES REPRESENTATIVE</text>
  <line class="title-rule" x1="1162" y1="300" x2="1265" y2="300"/>

  <text class="agent-phone" x="859" y="433" text-anchor="middle" textLength="717" lengthAdjust="spacingAndGlyphs">613.555.0187</text>

  <text class="tagline" x="892" y="520" text-anchor="middle" textLength="768" lengthAdjust="spacingAndGlyphs">FOCUSED, DRIVEN, AND <tspan class="emphasis">EXPERIENCED!</tspan></text>

  <g class="award wardens-guild">
    <circle class="badge-ring" cx="596" cy="612" r="57"/>
    <circle class="badge-core" cx="596" cy="612" r="38"/>
    <text class="brokerage" x="665" y="583" textLength="118" lengthAdjust="spacingAndGlyphs">HARBOURLINE REALTY</text>
    <text class="award-name" x="663" y="620" textLength="156" lengthAdjust="spacingAndGlyphs">WARDENS</text>
    <text class="award-name" x="663" y="655" textLength="62" lengthAdjust="spacingAndGlyphs">GUILD</text>
    <line class="award-rule" x1="731" y1="626" x2="731" y2="658"/>
    <text class="award-note" x="737" y="640" textLength="82" lengthAdjust="spacingAndGlyphs">NATIONAL TOP 1%</text>
    <text class="award-years" x="737" y="656" textLength="82" lengthAdjust="spacingAndGlyphs">2020 | 2022</text>
  </g>

  <g class="award summit-lantern">
    <circle class="badge-core" cx="895" cy="618" r="37"/>
    <text class="brokerage" x="939" y="574" textLength="130" lengthAdjust="spacingAndGlyphs">HARBOURLINE REALTY</text>
    <text class="award-name light" x="937" y="614" textLength="226" lengthAdjust="spacingAndGlyphs">SUMMIT LANTERN</text>
    <text class="award-name light" x="937" y="654" textLength="160" lengthAdjust="spacingAndGlyphs">AWARD 2022</text>
  </g>

  <g class="social-links">
    <text class="social-name" x="1205" y="611">Pagewall</text>
    <line class="social-rule" x1="1205" y1="624" x2="1340" y2="624"/>
    <text class="social-name" x="1205" y="652">Snapframe</text>
  </g>
</svg>
</body>
</html>
```